School Management website

I need page design for our school management system website

Base website is www.brindavo.com. When the student logs in, he will reach the below pages.
You can either design with white and blue background or grey and white background

Page 1 - School Info

Header
product name("Brindavo") in left corner
logout link in right corner

LeftMenu

Dashboard
School Info
School Settings
Staffs
Classes
Messaging
Contact Us

Footer
About link and copyright text

School Info content
The page should have breadcrumb

The content of this page will be the school profile
We have to show the school logo
Name
School Type
School Code
School Count
School Address
School phone 1&2
School Email
School Website

The page content should show edit school profile link which will take the user to another page

```html
<!DOCTYPE html>
<html lang="en">
<head>
<meta charset="utf-8">
<title>Brindavo – School Profile</title>
<link href="https://fonts.googleapis.com/css2?family=Montserrat:wght@400;500;600;700&display=swap" rel="stylesheet">
<style>
  :root {
    --brand-blue: #26a6df;
    --menu-blue: #47b2e4;
    --menu-active: #3aa9dd;
    --white: #ffffff;
    --ink: #333333;
    --muted: #555555;
    --field-border: #d9d9d9;
    --dark-button: #3a3a3a;
    --school-green: #6aa93f;
    --avatar-tone: #d9a77f;
  }
  * { box-sizing: border-box; margin: 0; padding: 0; }
  html, body { width: 1122px; height: 1200px; overflow: hidden; }
  body {
    position: relative;
    font-family: "Montserrat", sans-serif;
    background: var(--white);
    color: var(--ink);
  }

  /* Header */
  .site-header { position: absolute; left: 0; top: 0; width: 1122px; height: 91px; background: var(--white); }
  .brand {
    position: absolute; left: 173px; top: 50px;
    display: flex; align-items: center; gap: 7px;
    font-weight: 700; font-size: 20px; color: var(--brand-blue);
  }
  .brand-mark { width: 12px; height: 12px; background: var(--brand-blue); }
  .user-box { position: absolute; left: 818px; top: 22px; height: 50px; }
  .user-avatar {
    position: absolute; left: 0; top: 0; width: 50px; height: 50px; border-radius: 50%;
    border: 4px solid var(--brand-blue); background: var(--avatar-tone); z-index: 2;
  }
  .logout-button {
    position: absolute; left: 44px; top: 8px; width: 88px; height: 37px;
    background: var(--brand-blue); color: var(--white);
    font-weight: 600; font-size: 14px;
    display: flex; align-items: center; justify-content: center; gap: 5px; padding-left: 6px;
  }

  /* Main band */
  .main-band { position: absolute; left: 0; top: 91px; width: 1122px; height: 1053px; background: var(--brand-blue); }

  /* Side menu */
  .side-menu {
    position: absolute; left: 172px; top: 126px; width: 254px; height: 436px;
    background: var(--menu-blue); border: 1px solid rgba(255,255,255,0.7);
    list-style: none;
  }
  .menu-item {
    position: absolute; left: 0; width: 252px;
    color: var(--white); font-weight: 600; font-size: 16px;
    padding-left: 13px; display: flex; align-items: center;
    border-bottom: 1px dashed rgba(255,255,255,0.85);
  }
  .menu-item.is-active { background: var(--menu-active); }
  .menu-item.is-active::before {
    content: ""; position: absolute; left: -1px; top: 50%; margin-top: -4px;
    border-left: 5px solid var(--white); border-top: 4px solid transparent; border-bottom: 4px solid transparent;
  }
  .menu-item.is-last { border-bottom: none; }

  /* Breadcrumb + edit */
  .breadcrumb { position: absolute; left: 466px; top: 138px; color: var(--white); font-weight: 600; font-size: 14.5px; letter-spacing: 0.2px; }
  .edit-link {
    position: absolute; left: 838px; top: 136px; width: 116px; height: 23px;
    background: var(--dark-button); color: var(--white);
    font-size: 9.5px; font-weight: 600;
    display: flex; align-items: center; gap: 5px; padding-left: 4px;
  }

  /* Profile card */
  .profile-card { position: absolute; left: 466px; top: 174px; width: 488px; height: 932px; background: var(--white); }
  .school-logo {
    position: absolute; left: 27px; top: 22px;
    display: flex; align-items: center; gap: 6px;
    font-family: "Montserrat", sans-serif; font-weight: 600; font-size: 13px; color: var(--school-green);
  }
  .school-logo-mark { width: 14px; height: 14px; border-radius: 50%; background: var(--school-green); }
  .field-label { position: absolute; left: 27px; font-size: 11.5px; font-weight: 700; color: var(--ink); }
  .field-input {
    position: absolute; left: 27px; width: 432px; height: 39px;
    border: 1px solid var(--field-border); background: var(--white);
    font-size: 10px; color: var(--muted); padding: 0 7px;
    display: flex; align-items: center;
  }
  .field-input.is-textarea { align-items: flex-start; padding-top: 9px; height: 80px; }
  .field-input.is-select { justify-content: space-between; padding-right: 14px; }
  .submit-button {
    position: absolute; left: 27px; top: 876px; width: 98px; height: 39px;
    border: 2px solid var(--brand-blue); color: var(--brand-blue);
    font-weight: 700; font-size: 13px; letter-spacing: 0.5px;
    display: flex; align-items: center; justify-content: center;
  }

  /* Footer */
  .site-footer { position: absolute; left: 0; top: 1144px; width: 1122px; height: 56px; background: var(--white); }
  .footer-text { position: absolute; left: 171px; top: 19px; font-size: 12px; color: var(--muted); }
  .social-links { position: absolute; left: 917px; top: 19px; display: flex; gap: 2px; }
  .social-dot { width: 15px; height: 15px; border-radius: 50%; background: var(--ink); }
</style>
</head>
<body>
  <header class="site-header">
    <div class="brand"><span class="brand-mark"></span>Brindavo</div>
    <div class="user-box">
      <div class="user-avatar" role="img" aria-label="Student profile photo"></div>
      <div class="logout-button">Logout
        <svg width="8" height="6" viewBox="0 0 8 6"><path d="M0 0h8L4 6z" fill="#fff"/></svg>
      </div>
    </div>
  </header>

  <main class="main-band"></main>

  <ul class="side-menu">
    <li class="menu-item" style="top:0;height:52px;">Dashboard</li>
    <li class="menu-item is-active" style="top:52px;height:62px;">School Info</li>
    <li class="menu-item" style="top:114px;height:66px;">School Settings</li>
    <li class="menu-item" style="top:180px;height:62px;">Staffs</li>
    <li class="menu-item" style="top:242px;height:60px;">Classes</li>
    <li class="menu-item" style="top:302px;height:66px;">Messaging</li>
    <li class="menu-item is-last" style="top:368px;height:50px;">Contact Us</li>
  </ul>

  <nav class="breadcrumb">Student &gt; School Info &gt; School Profile</nav>
  <div class="edit-link">
    <svg width="13" height="13" viewBox="0 0 13 13" fill="none" stroke="#fff" stroke-width="1.3">
      <path d="M6 2H1.5v9.5H11V7"/><path d="M5 8l.5-2L11 .7l1.3 1.3L6.9 7.5z"/>
    </svg>
    Edit school profile
  </div>

  <section class="profile-card">
    <div class="school-logo"><span class="school-logo-mark"></span>Maple Grove School</div>

    <div class="field-label" style="top:112px;">Name</div>
    <div class="field-input" style="top:134px;">Type Name</div>

    <div class="field-label" style="top:195px;">School Type</div>
    <div class="field-input is-select" style="top:214px;">School Type
      <svg width="8" height="7" viewBox="0 0 8 7"><path d="M0 0h8L4 7z" fill="#333"/></svg>
    </div>

    <div class="field-label" style="top:279px;">School Code</div>
    <div class="field-input" style="top:301px;">Code</div>

    <div class="field-label" style="top:363px;">School Count</div>
    <div class="field-input" style="top:386px;">Count</div>

    <div class="field-label" style="top:448px;">School Address</div>
    <div class="field-input is-textarea" style="top:471px;">Type Address 1</div>

    <div class="field-label" style="top:573px;">School phone 1&amp;2</div>
    <div class="field-input" style="top:593px;">Phone 1</div>
    <div class="field-input" style="top:644px;">Phone 2</div>

    <div class="field-label" style="top:699px;">School Email</div>
    <div class="field-input" style="top:718px;">E-Mail</div>

    <div class="field-label" style="top:783px;">School Website</div>
    <div class="field-input" style="top:810px;">Website</div>

    <div class="submit-button">SUBMIT</div>
  </section>

  <footer class="site-footer">
    <div class="footer-text">About &nbsp;|&nbsp; Copyright © 2014 | All Rights Reserved</div>
    <div class="social-links">
      <span class="social-dot"></span><span class="social-dot"></span>
    </div>
  </footer>
</body>
</html>
```